Meadowlark Counseling Partners, LLC Needs Modern Business Card Design.

We provide behavioral health services from western Kansas to eastern Kansas. There is an abundance of competition for the services we provide with our main competitor being larger and having significantly more financial resources; however, the quality of services we provide is greater and we have started to catch the attention of the State of Kansas. We had a great logo designed by ArtFolio - this will be used to build upon our brand. The logo (attached) should be used in the card development. We want something unique, modern, but also a card design that clearly states our name, contact info, provides the name and unqiue location of each clinician, etc. Rounded edges, or a unique size, just something that makes our business card stand out from others. I have also uploaded each clinician's name and their unique location and phone number.

Our idea is to have one side be black with our logo. Then, on the other side have business cards for each individual. Plus, we want one card that is "generic" with no specific clinician's name listed so that we can give clients an appointment card when they leave. Some clinicians have two locations - we're open to design and background color, but we have started going with branding colors of black, the yellow in the logo files attached, and sometimes a gray. Our new office has been decorated using this theme.

Target Market(s)

individuals and families in need of behavioral health services; potential professional referral sources; existing referral sources

Industry/Entity Type

Business

Contact Information for Business Card

I attached a Word doc that provides clinician names, credentials and location information specific to each individual.

Font styles to use
Serif

Colors
000000
fbed22
dbdbdb
9d9d9d
c3c3c3

Requirements
Must have
• 1) use of the company logo that has been attached; 2) a template that provides us space to individualize business cards for all of our clinicians; 3) should stick to the colors we are branding with: black, yellow from the logo file, maybe a gray shade and we're open to a suggestion on a shade of white.
Nice to have
• Group discussion culminated in the thought that one side would be black with just our logo - no clinician names, etc. A unique design - rounded edges, unique size, some catchy lay-out would be nice.
Should not have
• Must not be too busy. Should look "clean." The project should stick to branding colors: black, yellow (from the logo file), maybe a gray and shade of white.

```html
<!DOCTYPE html>
<html lang="en">
<head>
<meta charset="utf-8">
<title>Meadowlark Counseling Partners – Business & Appointment Card</title>
<link rel="stylesheet" href="https://fonts.googleapis.com/css2?family=PT+Serif:ital,wght@0,400;0,700;1,400&display=swap">
<style>
  :root {
    --page: #e9e7e4;
    --black: #050505;
    --gold: #f5b61c;
    --white: #ffffff;
    --ink-light: #e4e4e4;
    --label: #6b6b6b;
    --rule: #c9c9c9;
    --divider-dark: #3a3a3a;
    --divider-light: #bdbdbd;
  }
  * { margin: 0; padding: 0; box-sizing: border-box; }
  html, body {
    width: 1200px; height: 1000px; overflow: hidden;
    background: var(--page);
    font-family: "PT Serif", Georgia, serif;
  }
  .card {
    position: absolute; left: 220px; width: 760px;
    border-radius: 24px; overflow: hidden;
    box-shadow: 0 6px 18px rgba(0,0,0,.25);
  }
  /* Front: black business card */
  .card--front {
    top: 50px; height: 435px;
    background: var(--black);
  }
  .card--front .gloss {
    position: absolute; inset: 0;
    background: linear-gradient(118deg, transparent 58%, rgba(255,255,255,.07) 58.2%, rgba(255,255,255,.12) 80%, rgba(255,255,255,.05) 100%);
  }
  .brand {
    position: absolute; text-align: center; color: var(--gold);
    font-weight: 400; letter-spacing: .06em; text-transform: uppercase;
  }
  .brand__mark {
    display: block; margin: 0 auto; border-radius: 50%; background: var(--gold);
  }
  .card--front .brand { left: 50px; top: 150px; width: 300px; font-size: 19px; line-height: 1.3; }
  .card--front .brand__mark { width: 60px; height: 60px; margin-bottom: 18px; }
  .divider { position: absolute; width: 1px; }
  .card--front .divider { left: 380px; top: 115px; height: 210px; background: var(--divider-dark); }
  .contact { position: absolute; left: 409px; top: 115px; color: var(--ink-light); font-size: 18px; line-height: 23px; }
  .contact__name { color: var(--gold); font-weight: 700; font-size: 21px; }
  .contact__block { margin-top: 25px; }
  .contact__block--tight { margin-top: 14px; }
  .accent { color: var(--gold); }

  /* Back: appointment card */
  .card--back {
    top: 523px; height: 437px;
    background: var(--white);
  }
  .card--back .brand { left: 52px; top: 52px; width: 190px; font-size: 12px; line-height: 1.3; }
  .card--back .brand__mark { width: 30px; height: 30px; margin-bottom: 10px; }
  .card--back .divider { left: 249px; top: 78px; height: 55px; background: var(--divider-light); }
  .appt-heading { position: absolute; left: 272px; top: 77px; }
  .appt-heading__kicker { color: var(--label); font-weight: 700; font-size: 17px; line-height: 20px; }
  .appt-heading__title { color: var(--gold); font-weight: 700; font-size: 31px; line-height: 35px; }
  .field { position: absolute; left: 271px; display: flex; align-items: flex-end; color: var(--label); font-size: 15px; }
  .field__line { border-bottom: 1px solid var(--rule); height: 1px; margin: 0 0 4px 8px; }
  .field__suffix { margin-left: 6px; }
  .swoosh { position: absolute; left: 0; bottom: 0; width: 760px; height: 437px; }
  .tagline {
    position: absolute; right: 30px; bottom: 22px;
    color: var(--gold); font-style: italic; font-size: 21px;
  }
</style>
</head>
<body>

<section class="card card--front" aria-label="Business card front">
  <div class="gloss"></div>
  <div class="brand">
    <span class="brand__mark"></span>
    Meadowlark Counseling Partners, LLC
  </div>
  <div class="divider"></div>
  <div class="contact">
    <div class="contact__name">Daniel R. Hartwell, LP</div>
    <div>President</div>
    <div class="contact__block">418 N. Prairie Ln.<br>Hays, Kansas 67601</div>
    <div class="contact__block contact__block--tight">
      <span class="accent">P</span>: (785) 555-0142<br>
      <span class="accent">E</span>: info@youremail.com<br>
      www.<span class="accent">yourwebsite</span>.com
    </div>
  </div>
</section>

<section class="card card--back" aria-label="Appointment card">
  <svg class="swoosh" viewBox="0 0 760 437" aria-hidden="true">
    <path d="M190 437 C 330 385 560 352 760 345 L760 437 Z" fill="var(--black)"/>
  </svg>
  <div class="brand">
    <span class="brand__mark"></span>
    Meadowlark Counseling Partners, LLC
  </div>
  <div class="divider"></div>
  <div class="appt-heading">
    <div class="appt-heading__kicker">Your Next</div>
    <div class="appt-heading__title">Appointment</div>
  </div>
  <div class="field" style="top:160px">For<span class="field__line" style="width:342px"></span></div>
  <div class="field" style="top:200px">With<span class="field__line" style="width:326px"></span></div>
  <div class="field" style="top:240px">Date<span class="field__line" style="width:330px"></span></div>
  <div class="field" style="top:280px">Time<span class="field__line" style="width:277px"></span><span class="field__suffix">am/pm</span></div>
  <div class="tagline">“Find your way forward.”</div>
</section>

</body>
</html>
```